National Golf Software business needs banner ad designs

Our software company looks after golf clubs throughout the country. Our service specialises in membership billing for the clubs and tries to convince members to change from paying their fees upfront to monthly payment by direct debit. Simple catch cries like "spread the cost of your membership across the whole year", "let us help you make your membership affordable", "Ask you club how to spread the cost of your subs" etc. We are dealing with cost conscious clubs - not the top end of the market - and their members are also cost conscious. No good being too 'high brow'. We are also dealing with older members who are fearful of change and afraid of technology - we need to be safe and reassuring yet a great way to save up front costs. We need probably 5 to 10 banners that can rotate through on our website and on our mobile product.

Target Market(s)

Golfers, typically older and afraid of technology and afraid of direct debit. Existing members of golf clubs who have paid upfront for years and don't understand why they should pay a few dollars extra each month to split their payments. Sometimes their annual fees are quite low ($300 - $400) so they cannot justify the additional $3.50 per month surcharge for splitting their fees.

Industry/Entity Type

Golf Course

Requirements
Must have
• Make the member desire to spread the cost of their annual subscriptions. Safe, reliable, frees up their disposable income. Talk to the club to find out how. Safe and secure. Club administered.
Nice to have
• Option to call us directly on a 1300 582 916 number - they will still need to go back to the club to fill in and lodge the paperwork.
Should not have
• Cheesy, in your face, aggressive

```html
<!DOCTYPE html>
<html lang="en">
<head>
<meta charset="UTF-8">
<title>Spread the Cost of Your Membership</title>
<link rel="stylesheet" href="https://fonts.googleapis.com/css2?family=Open+Sans:wght@700;800&display=swap">
<style>
  :root {
    --grass-dark: #2f5a1c;
    --grass-mid: #5e8a34;
    --grass-light: #8cae55;
    --panel-green: rgba(52, 88, 24, 0.88);
    --accent-navy: #1d2c5e;
    --cta-red: #d8201c;
    --white: #ffffff;
    --brand-blue: #1f4f8f;
  }
  html, body {
    margin: 0;
    padding: 0;
    overflow: hidden;
    background: #ffffff;
  }
  .banner {
    position: relative;
    width: 1200px;
    height: 200px;
    overflow: hidden;
    font-family: "Open Sans", Arial, sans-serif;
  }
  .banner__scene {
    position: absolute;
    inset: 0;
    background:
      radial-gradient(ellipse 160px 120px at 60px 60px, rgba(235, 235, 230, 0.55), transparent 70%),
      radial-gradient(ellipse 200px 200px at 120px 170px, rgba(170, 170, 165, 0.5), transparent 70%),
      linear-gradient(180deg, var(--grass-light) 0%, var(--grass-mid) 45%, var(--grass-dark) 100%);
  }
  .headline {
    position: absolute;
    left: 250px;
    top: 0;
    width: 680px;
    height: 100px;
    margin: 0;
    background: var(--panel-green);
    color: var(--white);
    font-size: 28px;
    font-weight: 700;
    line-height: 42px;
    text-align: center;
    white-space: nowrap;
    display: flex;
    flex-direction: column;
    justify-content: center;
  }
  .headline__accent {
    color: var(--accent-navy);
  }
  .cta {
    position: absolute;
    left: 250px;
    top: 118px;
    width: 680px;
    height: 60px;
    background: var(--cta-red);
    color: var(--white);
    font-size: 27px;
    font-weight: 700;
    line-height: 60px;
    text-align: center;
    white-space: nowrap;
    letter-spacing: 0.3px;
  }
  .brand {
    position: absolute;
    left: 970px;
    top: 6px;
    width: 222px;
    height: 188px;
    background: var(--white);
    border-radius: 22px;
    display: flex;
    flex-direction: column;
    align-items: center;
    justify-content: center;
    gap: 14px;
  }
  .brand__dot {
    width: 34px;
    height: 34px;
    border-radius: 50%;
    background: var(--brand-blue);
  }
  .brand__name {
    color: var(--brand-blue);
    font-size: 28px;
    font-weight: 700;
    line-height: 32px;
    text-align: center;
  }
</style>
</head>
<body>
  <div class="banner">
    <div class="banner__scene" role="img" aria-label="Close-up of a golf ball and wedge resting on green grass"></div>
    <h1 class="headline">
      <span>Spread the Cost of Your Membership</span>
      <span>across the <span class="headline__accent">Whole Year</span></span>
    </h1>
    <div class="cta">CALL YOUR CLUB TO FIND OUT HOW</div>
    <div class="brand">
      <span class="brand__dot"></span>
      <span class="brand__name">Greenlink<br>Billing</span>
    </div>
  </div>
</body>
</html>
```